Security Warning Sign

We have an existing sign that needs an update. I have attached a picture of the current square sign. We need to maintain the same wording. It needs to be professional and appropriate to attach to our customers fence. Also attached is a copy of our building sign which may lend some inspiration and hopefully the ai format will assist. The final sign will be 600mm x 600mmOur website is www.halvorngate.com.au

```html
<!DOCTYPE html>
<html lang="en">
<head>
<meta charset="utf-8">
<title>Security Warning Sign – Halvorngate Security</title>
<link rel="stylesheet" href="https://fonts.googleapis.com/css2?family=Arimo:wght@700&family=Jost:wght@500&family=Ubuntu:wght@500;700&display=swap">
<style>
  :root {
    --orange: #ff6a00;
    --charcoal: #1a1d1e;
    --charcoal-deep: #111415;
    --white: #ffffff;
  }
  * { margin: 0; padding: 0; box-sizing: border-box; }
  html, body { width: 1200px; height: 1200px; overflow: hidden; background: var(--charcoal); }
  .sign {
    position: relative; width: 1200px; height: 1200px;
    background: linear-gradient(135deg, var(--charcoal-deep), var(--charcoal) 50%, var(--charcoal-deep));
  }
  .frame {
    position: absolute; left: 58px; top: 55px; width: 1089px; height: 1089px;
    background: var(--orange);
  }
  .headline {
    position: absolute; left: 0; top: 92px; width: 100%;
    font-family: "Arimo", Arial, sans-serif; font-weight: 700; font-size: 200px;
    line-height: 1; color: var(--white); text-align: center; letter-spacing: -1px;
  }
  .panel {
    position: absolute; left: 73px; top: 324px; width: 1061px; height: 806px;
    background: linear-gradient(160deg, var(--charcoal-deep), var(--charcoal) 60%, #141718);
  }
  .camera-art {
    position: absolute; left: 73px; top: 377px; width: 350px; height: 340px;
    background: var(--orange); border-radius: 10px;
  }
  .notice {
    position: absolute; right: 96px; top: 464px;
    font-family: "Jost", Futura, sans-serif; font-weight: 500; font-size: 76px;
    line-height: 87px; color: var(--white); text-align: right; text-transform: uppercase;
  }
  .brand {
    position: absolute; left: 194px; top: 964px; display: flex; align-items: center; gap: 14px;
  }
  .brand-dot { width: 100px; height: 100px; border-radius: 50%; background: var(--orange); }
  .brand-name {
    font-family: "Ubuntu", sans-serif; font-weight: 700; font-size: 29px;
    line-height: 28px; color: var(--white); letter-spacing: 1px;
  }
  .contact-label {
    position: absolute; left: 695px; top: 945px;
    font-family: "Ubuntu", sans-serif; font-weight: 700; font-size: 25px;
    color: var(--white); letter-spacing: 2.5px;
  }
  .phone-band { position: absolute; left: 645px; top: 987px; width: 489px; height: 74px; }
  .phone-band svg { position: absolute; inset: 0; }
  .phone-number {
    position: absolute; left: 90px; top: 14px;
    font-family: "Ubuntu", sans-serif; font-weight: 700; font-size: 43px;
    line-height: 46px; color: var(--white);
  }
  .website {
    position: absolute; left: 694px; top: 1078px;
    font-family: "Ubuntu", sans-serif; font-weight: 500; font-size: 25px;
    color: var(--orange); letter-spacing: 0.2px;
  }
</style>
</head>
<body>
<main class="sign">
  <div class="frame"></div>
  <h1 class="headline">WARNING</h1>
  <section class="panel"></section>
  <div class="camera-art" role="img" aria-label="Illustration of a wall-mounted CCTV security camera"></div>
  <p class="notice">Electronic<br>Surveillance<br>and Recording<br>Devices Installed<br>in this Area</p>

  <div class="brand">
    <span class="brand-dot"></span>
    <span class="brand-name">HALVORNGATE<br>SECURITY<br>SERVICES</span>
  </div>

  <p class="contact-label">HALVORNGATE SECURITY</p>
  <div class="phone-band">
    <svg width="489" height="74" viewBox="0 0 489 74" aria-hidden="true">
      <polygon points="43,0 489,0 489,74 0,74" fill="var(--orange)"/>
      <g fill="var(--white)" transform="translate(42,17) scale(1.05)">
        <path d="M30 4c3 2 5 5 4 8l-5 5c-1 1-1 2 0 3l0 0c-2 4-6 9-10 12-1 1-2 1-3 0l-5 4c-3 1-7-1-9-4 3 1 5 1 7-1 7-5 14-13 19-21 2-3 2-5 2-6z"/>
        <path d="M18 6a14 14 0 0 0-14 14h3a11 11 0 0 1 11-11z"/>
        <path d="M18 12a8 8 0 0 0-8 8h3a5 5 0 0 1 5-5z"/>
      </g>
    </svg>
    <span class="phone-number">1300 555 017</span>
  </div>
  <p class="website">www.halvorngate.com.au</p>
</main>
</body>
</html>
```